Remote Planning & Scheduling Power Point Presentation

This PP presentation is to help explain what RPS is and its benefits. Need help with a better illustration on slide 3 that explains the process, overall aesthetics, need better images, and cleaner workflow on slide 18. Keep the DEW Logo in the bottom right of each slide. I have included a one-pager and infographic to help. I am still working of verbiage.

Thanks
SL

```html
<!DOCTYPE html>
<html lang="en">
<head>
<meta charset="utf-8">
<title>Keeping Everyone Connected – Remote Planning</title>
<link rel="stylesheet" href="https://fonts.googleapis.com/css2?family=Questrial&family=Carlito:wght@400;700&display=swap">
<style>
  :root {
    --navy: #0a2d82;
    --navy-deep: #062a7a;
    --slate: #47505c;
    --orange: #f7941d;
    --page: #ffffff;
    --ink: #111111;
    --logo-grey: #b8c2d1;
    --frame: #0d2f86;
  }
  * { margin: 0; padding: 0; box-sizing: border-box; }
  html, body { width: 1200px; height: 708px; overflow: hidden; background: var(--page); }
  .slide { position: relative; width: 1200px; height: 708px; background: var(--page); font-family: "Carlito", "Calibri", sans-serif; }

  .header { position: absolute; left: 22px; top: 17px; width: 1163px; height: 181px; }
  .header svg { position: absolute; inset: 0; }
  .header-shadow { position: absolute; left: 22px; top: 198px; width: 1163px; height: 8px;
    background: linear-gradient(#d9dce2, rgba(255,255,255,0)); }
  .slide-title { position: absolute; left: 106px; top: 74px; font-family: "Questrial", sans-serif;
    font-size: 48px; color: #ffffff; letter-spacing: 1px; font-weight: 400; }
  .slide-tag { position: absolute; left: 874px; top: 124px; font-family: "Carlito", sans-serif;
    font-weight: 700; font-size: 29px; color: var(--ink); }

  .label { position: absolute; height: 31px; background: var(--navy-deep); color: #fff;
    font-size: 19px; display: flex; align-items: center; justify-content: center; }
  .frame { position: absolute; border: 3px solid var(--frame); padding: 6px; background: #fff; }
  .frame .fill { width: 100%; height: 100%; }

  .leadership-label { left: 159px; top: 219px; width: 184px; }
  .leadership-frame { left: 162px; top: 261px; width: 180px; height: 125px; }
  .leadership-frame .fill { background: linear-gradient(135deg, #c9c2b4, #7e6a5a 55%, #3f3a3a); }

  .onsite-label { left: 477px; top: 219px; width: 185px; }
  .onsite-frame { left: 480px; top: 263px; width: 180px; height: 123px; }
  .onsite-frame .fill { background: linear-gradient(160deg, #8aa4b8, #4d6276 55%, #2c3a48); }

  .package-label { left: 775px; top: 219px; width: 261px; }
  .package-frame { left: 775px; top: 263px; width: 261px; height: 125px; }
  .package-frame .fill { background: linear-gradient(180deg, #f3f5f7, #e6ebdf 60%, #d7e6b9); }

  .sto-label { left: 477px; top: 491px; width: 185px; }
  .sto-frame { left: 474px; top: 542px; width: 192px; height: 95px; }
  .sto-frame .fill { background: linear-gradient(180deg, #eef2f6, #dbe6ee); }

  .remote-label { left: 781px; top: 477px; width: 250px; }
  .remote-frame { left: 785px; top: 515px; width: 244px; height: 131px; }
  .remote-frame .fill { background: linear-gradient(180deg, #e8eef1, #a9c4cc 60%, #6f8f99); }

  .task-box { position: absolute; left: 152px; top: 469px; width: 199px; height: 188px;
    border: 3px double var(--frame); display: flex; align-items: center; justify-content: center; }
  .task-list { list-style: none; text-align: center; color: var(--navy); font-size: 17.5px; line-height: 22px; }

  .flow-arrows { position: absolute; inset: 0; pointer-events: none; }
  .brand { position: absolute; left: 1102px; top: 606px; font-family: "Carlito", sans-serif;
    font-weight: 700; font-size: 30px; color: var(--logo-grey); letter-spacing: 1px; }
</style>
</head>
<body>
<main class="slide">
  <header>
    <div class="header">
      <svg width="1163" height="181" viewBox="0 0 1163 181">
        <rect width="1163" height="181" fill="var(--slate)"/>
        <polygon points="0,0 878,0 754,181 0,181" fill="var(--navy)"/>
      </svg>
    </div>
    <div class="header-shadow"></div>
    <h1 class="slide-title">Keeping Everyone Connected</h1>
    <p class="slide-tag">Remote Planning</p>
  </header>

  <div class="label leadership-label">Leadership Team</div>
  <div class="frame leadership-frame"><div class="fill" role="img" aria-label="Photo of a leadership team meeting around a table"></div></div>

  <div class="label onsite-label">On Site Planner</div>
  <div class="frame onsite-frame"><div class="fill" role="img" aria-label="Photo of site planners in hard hats at an industrial plant"></div></div>

  <div class="label package-label">Complete Work Package</div>
  <div class="frame package-frame"><div class="fill" role="img" aria-label="Screenshot of a work package schedule with Gantt chart"></div></div>

  <div class="label sto-label">STO Planner</div>
  <div class="frame sto-frame"><div class="fill" role="img" aria-label="Screenshot of a planning dashboard"></div></div>

  <div class="label remote-label">Remote Planner Team</div>
  <div class="frame remote-frame"><div class="fill" role="img" aria-label="Photo of a remote planning office with workstations"></div></div>

  <div class="task-box">
    <ul class="task-list">
      <li>Monitor Progress</li>
      <li>Review Content</li>
      <li>Track FEL</li>
      <li>Assignments</li>
      <li>Develop</li>
      <li>Budgets Share</li>
      <li>with Stakeholders</li>
    </ul>
  </div>

  <svg class="flow-arrows" width="1200" height="708" viewBox="0 0 1200 708" fill="var(--orange)">
    <!-- leadership ↔ on site -->
    <polygon points="346,325 376,302 376,316 436,316 436,302 466,325 436,348 436,334 376,334 376,348"/>
    <!-- work package → on site -->
    <polygon points="678,323 708,300 708,314 759,314 759,332 708,332 708,346"/>
    <!-- on site → STO -->
    <polygon points="561,397 579,397 579,433 593,433 570,462 547,433 561,433"/>
    <!-- remote team → work package -->
    <polygon points="898,462 916,462 916,435 930,435 907,406 884,435 898,435"/>
    <!-- tasks → leadership -->
    <polygon points="242,462 260,462 260,432 274,432 251,403 228,432 242,432"/>
    <!-- STO → tasks -->
    <polygon points="369,574 399,551 399,565 450,565 450,583 399,583 399,597"/>
    <!-- STO → remote team -->
    <polygon points="764,574 734,551 734,565 680,565 680,583 734,583 734,597"/>
  </svg>

  <div class="brand">DEW</div>
</main>
</body>
</html>
```